Strong, modern, clean Business Card design

Looking for a stunning, but CLEAN business card design. While we are a faith-based organization, we do NOT want this to look religious.

Industry/Entity Type

Non-Profit

Contact Information for Business Card

Dale Munroe | Lead Pastor
dale@BrightHarvestHope.org
970-555-0148
PO Box 7316
Alder Springs, OR 80571

Font styles to use
Serif
Sans Serif

Requirements
Should not have
• Religious imagery or symbolism

```html
<!DOCTYPE html>
<html lang="en">
<head>
<meta charset="UTF-8">
<title>Renewal Commons – Business Card</title>
<link rel="stylesheet" href="https://fonts.googleapis.com/css2?family=Source+Sans+3:wght@400;600&display=swap">
<style>
  :root {
    --backdrop: #1b1c1e;
    --card: #2b2c30;
    --brand-blue: #2b90d9;
    --soft-white: #e4e8ee;
  }
  * { margin: 0; padding: 0; box-sizing: border-box; }
  html, body {
    width: 1200px;
    height: 900px;
    overflow: hidden;
    background: var(--backdrop);
  }
  .stage {
    width: 1200px;
    height: 900px;
    display: flex;
    align-items: center;
    justify-content: center;
  }
  .business-card {
    position: relative;
    width: 1050px;
    height: 600px;
    background: var(--card);
    border-radius: 6px;
    font-family: "Source Sans 3", "Myriad Pro", sans-serif;
  }
  .brand-name {
    position: absolute;
    top: 120px;
    left: 0;
    right: 0;
    text-align: center;
    color: var(--brand-blue);
    font-weight: 600;
    font-size: 84px;
    letter-spacing: 6px;
    text-transform: uppercase;
    line-height: 1;
  }
  .divider {
    position: absolute;
    top: 262px;
    left: 150px;
    width: 750px;
    height: 4px;
    background: var(--brand-blue);
  }
  .contact {
    position: absolute;
    top: 300px;
    left: 0;
    right: 0;
    text-align: center;
    list-style: none;
    font-size: 30px;
    line-height: 40px;
    color: var(--brand-blue);
  }
  .contact .city { color: var(--soft-white); }
</style>
</head>
<body>
  <main class="stage">
    <article class="business-card">
      <h1 class="brand-name">Renewal Commons</h1>
      <div class="divider"></div>
      <ul class="contact">
        <li class="name-title">Dale Munroe | Lead Pastor</li>
        <li class="email">dale@BrightHarvestHope.org</li>
        <li class="phone">541-555-0148</li>
        <li class="po-box">PO Box 7316</li>
        <li class="city">Alder Springs, OR 80571</li>
      </ul>
    </article>
  </main>
</body>
</html>
```